Heater product information sheets

I need the two product information sheets organized and laid out in a clean, easy to read attractive manner. These sheets are to advertise propane heaters for outdoor use and for wholesale to propane distributors, restaurants and homeowners that need to have propane heat as the winter ends and spring begins. They will be used for chilly evenings when people want to be outside eating, drinking and being social.
Updates

Low design quality

Target Market(s)

Restaurants, hospitality industry, special events, party rental companies, home owners with backyards

Font styles to use
Sans Serif

Requirements
Must have
• My logo in the document instead of r. Kolby and company
Nice to have
• I would like to see Fire illustrated coming up the heaters and on the round glass, show it up the middle of the glass tube propane heater.

```html
<!DOCTYPE html>
<html lang="en">
<head>
<meta charset="utf-8">
<title>Outdoor Propane Heater – Product Sheet</title>
<link href="https://fonts.googleapis.com/css2?family=Montserrat:wght@400;500;600;700&display=swap" rel="stylesheet">
<style>
:root{
  --orange:#f7941d;
  --white:#ffffff;
  --ink:#222222;
  --ink-soft:#444444;
  --row-grey:#e1e1e3;
  --row-light:#f4f4f5;
  --shadow-grey:#dcdcdc;
  --backdrop:#efece8;
  --heater-dark:#1d1d22;
  --heater-steel:#c9cbcf;
}
*{margin:0;padding:0;box-sizing:border-box}
html,body{width:1200px;height:1200px;overflow:hidden;background:var(--backdrop)}
body{font-family:'Montserrat',sans-serif;color:var(--ink);position:relative}
.sheet{position:absolute;left:210px;top:30px;width:786px;height:1112px;background:var(--white)}
.sheet > *{position:absolute}
.title-band{left:0;top:35px;width:604px;height:69px;background:var(--orange);color:var(--white);
  font-size:37px;font-weight:700;line-height:69px;padding-left:95px;letter-spacing:.3px}
.section-head{top:154px;font-size:14px;font-weight:700;color:var(--orange);letter-spacing:.2px}
.section-head.spec{left:98px}
.section-head.details{left:482px}
.rule{height:2px;background:var(--orange);top:175px}
.rule.spec{left:0;width:226px}
.rule.details{left:482px;width:304px}
.leaders{left:0;top:0;width:786px;height:700px}
.product-photo{left:280px;top:150px;width:178px;height:480px;border-radius:6px;
  background:linear-gradient(180deg,var(--heater-steel) 0%,#8f9297 18%,var(--heater-dark) 45%,var(--heater-dark) 100%)}
.spec-label{font-size:14px;font-weight:700;line-height:16px;text-align:right;color:var(--ink)}
.spec-label.btu{right:610px;top:244px}
.spec-label.finish{right:558px;top:340px}
.spec-label.tank{right:625px;top:424px}
.cert-badge{left:57px;top:527px;width:242px;height:90px}
.cert-text{left:73px;top:546px;font-size:13.5px;font-weight:700;line-height:16px;color:var(--white)}
.details-table{left:482px;top:177px;width:272px;height:349px;background:var(--row-grey);padding-top:13px;list-style:none}
.details-table li{font-size:12.5px;line-height:14.5px;color:var(--ink);padding:5px 8px 5px 28px;position:relative}
.details-table li::before{content:"";position:absolute;left:12px;top:10px;width:5px;height:5px;background:var(--orange)}
.details-table li.light{background:var(--row-light)}
.details-table li.tall{padding-top:7px;padding-bottom:8px}
.use-band{left:55px;top:681px;width:678px;height:162px;background:var(--orange);padding:29px 0 0 78px}
.use-band p{display:flex;align-items:center;gap:14px;color:var(--white);font-size:18.5px;font-weight:700;letter-spacing:.2px;height:37px}
.use-band svg{width:30px;height:26px;flex:none}
.note-head{left:69px;top:888px;font-size:14px;font-weight:700;color:var(--orange)}
.price{left:69px;top:916px;font-size:19px;color:var(--ink-soft)}
.note-small{left:69px;top:950px;font-size:12.5px;line-height:15px;color:var(--ink)}
.contact-shadow{left:423px;top:877px;width:302px;height:185px;background:var(--shadow-grey)}
.contact-box{left:430px;top:869px;width:303px;height:183px;background:var(--white);border:1.5px solid var(--orange);padding:12px 0 0 28px}
.contact-box h3{font-size:15px;font-weight:700;color:var(--orange)}
.contact-box .company{font-size:12.5px;font-weight:700;margin:10px 0 18px -2px}
.contact-row{display:flex;align-items:center;gap:10px;font-size:12.5px;height:29px;margin-left:-2px}
.contact-row svg{width:16px;height:16px;flex:none}
</style>
</head>
<body>
<main class="sheet">
  <h1 class="title-band">Outdoor Propane Heater</h1>

  <h2 class="section-head spec">SPECIFICATIONS</h2>
  <div class="rule spec"></div>
  <h2 class="section-head details">ADDITIONAL DETAILS</h2>
  <div class="rule details"></div>

  <div class="product-photo" role="img" aria-label="Photo of a tall black patio heater with a steel reflector top"></div>

  <svg class="leaders" viewBox="0 0 786 700" aria-hidden="true">
    <g fill="none" stroke="#f7941d" stroke-width="1.3">
      <polyline points="193,251 193,283 320,322"/>
      <polyline points="245,348 245,378 323,410"/>
      <polyline points="189,434 223,435 320,472"/>
    </g>
    <g fill="#f7941d">
      <rect x="189" y="247" width="8" height="8"/>
      <rect x="241" y="344" width="8" height="8"/>
      <rect x="185" y="430" width="8" height="8"/>
    </g>
  </svg>

  <p class="spec-label btu">Powerful<br>48,000 BTU</p>
  <p class="spec-label finish">Black Powder<br>Coated Finish</p>
  <p class="spec-label tank">Uses 20 lbs.<br>Propane Tank</p>

  <svg class="cert-badge" viewBox="0 0 242 90" aria-hidden="true">
    <polygon points="0,0 210,0 242,45 210,90 0,90" fill="#f7941d"/>
    <g fill="#ffffff">
      <circle cx="186" cy="35" r="13"/>
      <polygon points="178,44 171,66 178,62 182,69 188,48"/>
      <polygon points="194,44 201,66 194,62 190,69 184,48"/>
    </g>
    <circle cx="186" cy="35" r="6" fill="#f7941d"/>
  </svg>
  <p class="cert-text">CE, GS, AGA, CSA,<br>with ETL certificate<br>and ROHS approved.</p>

  <ul class="details-table">
    <li class="light">Commercial Quality</li>
    <li>For Outdoor Use Only</li>
    <li class="light tall">Conforms to ANSI STD Z83.26-2014<br>Certified to CSA STD 2.37-2014 Gas-<br>fired outdoor infrared patio heaters</li>
    <li class="tall">Safety Auto Shut Off Switch</li>
    <li class="light">Thermostatic Control</li>
    <li class="tall">Base Diameter 17" - Anti-Tip Design</li>
    <li class="light">Standard Wheels - Tilt &amp; Move</li>
    <li class="tall">Run time: 8-10 hours with standard<br>20 lbs. Propane tank</li>
    <li class="light">88" Tall</li>
    <li class="tall">Heating Area: 200 sq. ft</li>
  </ul>

  <section class="use-band">
    <p><svg viewBox="0 0 30 26" aria-hidden="true"><polyline points="3,13 11,21 27,4" fill="none" stroke="#fff" stroke-width="5"/></svg>RENTALS FOR LIVE EVENTS</p>
    <p><svg viewBox="0 0 30 26" aria-hidden="true"><polyline points="3,13 11,21 27,4" fill="none" stroke="#fff" stroke-width="5"/></svg>RENTALS FOR RESTAURANTS &amp; CATERING HALLS</p>
    <p><svg viewBox="0 0 30 26" aria-hidden="true"><polyline points="3,13 11,21 27,4" fill="none" stroke="#fff" stroke-width="5"/></svg>PURCHASE FOR YOUR HOME OR BUSINESS</p>
  </section>

  <h3 class="note-head">NOTE</h3>
  <p class="price">Price: Starting at $250 each</p>
  <p class="note-small">Assembly &amp; Delivery available upon request<br>Discounts for large quantity orders</p>

  <div class="contact-shadow"></div>
  <address class="contact-box" style="font-style:normal">
    <h3>To Rent or Purchase:</h3>
    <p class="company">R. Kolby &amp; Company</p>
    <p class="contact-row"><svg viewBox="0 0 16 16" aria-hidden="true"><rect x="4" y="2" width="8" height="12" rx="1.5" fill="none" stroke="#f7941d" stroke-width="1.6"/><circle cx="8" cy="11" r="1" fill="#f7941d"/></svg>555-014-2290</p>
    <p class="contact-row"><svg viewBox="0 0 16 16" aria-hidden="true"><rect x="1" y="3.5" width="14" height="9" fill="none" stroke="#f7941d" stroke-width="1.4"/><polyline points="1,3.5 8,9 15,3.5" fill="none" stroke="#f7941d" stroke-width="1.4"/></svg>Dana@RKeventrental.com</p>
    <p class="contact-row"><svg viewBox="0 0 16 16" aria-hidden="true"><path d="M8 1a5 5 0 0 0-5 5c0 4 5 9 5 9s5-5 5-9a5 5 0 0 0-5-5z" fill="#f7941d"/><circle cx="8" cy="6" r="2" fill="#fff"/></svg>42 Orchard Lane Millbrook, NJ 07000</p>
  </address>
</main>
</body>
</html>
```